Produkt-Etiketten-Design für Wagyu-Bolognese-Sauce
Zielgruppe
Wir sind ein landwirtschaftliches Unternehmen und züchten Wagyu Rinder und betreiben einen Online Shop.
Unsere Produktpallete beinhaltet Tk und frisch Fleisch und nun wollen wir unser Palette um Convinienc Food erweitern und dafür brauchen wir Etiketten.
Aufgabenstellung
Es sollte optisch zu unserem webauftritt und unserer Linie passen.
Wir brauchen Produkt Etikett für Wagyu Bolognese Sauce.
Gläser Maße hier entnehmen - https://www.glasoruma.com/sturzglas-435ml-weissglas-mdg.-to82-karton-64stk.html
Wir bauchen auch eine Zutaten-und Nährwerttabelle

```html
<!DOCTYPE html>
<html lang="de">
<head>
<meta charset="utf-8">
<title>Wagyu Bolognese Sauce – Etikettenalternativen</title>
<link rel="stylesheet" href="https://fonts.googleapis.com/css2?family=Open+Sans:wght@300;400;600;700&family=Ubuntu:wght@400;500;700&display=swap">
<style>
  :root {
    --bg: #ffffff;
    --ink: #111111;
    --label-black: #050505;
    --brand-red: #c8203f;
    --white: #ffffff;
    --marble-dark: #2c0a15;
    --marble-mid: #4a1424;
    --marble-light: #6b2436;
    --closure-red: #b51f3e;
    --closure-black: #1a0a0e;
  }
  * { margin: 0; padding: 0; box-sizing: border-box; }
  html, body { width: 1200px; height: 1200px; overflow: hidden; background: var(--bg); }
  .sheet { position: relative; width: 1200px; height: 1200px; font-family: "Open Sans", sans-serif; color: var(--ink); }

  .variant-title {
    position: absolute; top: 14px;
    font-family: "Ubuntu", sans-serif; font-weight: 700; font-size: 17.5px; letter-spacing: -0.2px;
  }
  .row-caption {
    position: absolute; left: 45px;
    font-family: "Open Sans", sans-serif; font-weight: 400; font-size: 16.5px; letter-spacing: 0.3px;
    transform: translate(-50%, -50%) rotate(-90deg); white-space: nowrap;
  }
  .closure { position: absolute; width: 338px; height: 30px; border-radius: 10px; }
  .closure--red { background: var(--closure-red); }
  .closure--black { background: var(--closure-black); }

  .label { position: absolute; width: 280px; height: 397px; overflow: visible; }

  .brand-name { font-family: "Open Sans", sans-serif; font-weight: 700; fill: var(--brand-red); }
  .tagline { font-family: "Open Sans", sans-serif; font-weight: 400; fill: var(--white); }
  .arc-text { font-family: "Ubuntu", sans-serif; }
  .arc-text--light { font-weight: 400; }
  .arc-text--bold { font-weight: 700; }
  .fill-red { fill: var(--brand-red); }
  .fill-white { fill: var(--white); }
</style>
</head>
<body>
<main class="sheet">

  <svg width="0" height="0" style="position:absolute" aria-hidden="true">
    <defs>
      <radialGradient id="marble" cx="50%" cy="45%" r="65%">
        <stop offset="0" stop-color="var(--marble-mid)"/>
        <stop offset="0.7" stop-color="var(--marble-dark)"/>
        <stop offset="1" stop-color="var(--marble-light)"/>
      </radialGradient>
      <radialGradient id="marble-soft" cx="50%" cy="50%" r="60%">
        <stop offset="0" stop-color="#3f1120"/>
        <stop offset="1" stop-color="#2a0913"/>
      </radialGradient>
      <clipPath id="label-clip"><rect x="0" y="0" width="389" height="620" rx="12"/></clipPath>
      <path id="arc-top" d="M 34 374 A 160 160 0 0 1 354 374"/>
      <path id="arc-bottom" d="M 6 374 A 188 188 0 0 0 382 374"/>
    </defs>
  </svg>

  <h2 class="variant-title" style="left:120px">1- Alternatives Design</h2>
  <h2 class="variant-title" style="left:498px">2- Alternatives Design</h2>
  <h2 class="variant-title" style="left:855px">3- Alternatives Design</h2>

  <p class="row-caption" style="top:333px">ROTER FLASCHENVERSCHLUSS</p>
  <p class="row-caption" style="top:930px">SCHWARZER FLASCHENVERSCHLUSS</p>

  <!-- Row: red closure -->
  <div class="closure closure--red" style="left:93px; top:70px"></div>
  <div class="closure closure--red" style="left:466px; top:70px"></div>
  <div class="closure closure--red" style="left:834px; top:70px"></div>

  <!-- Row: black closure -->
  <div class="closure closure--black" style="left:93px; top:668px"></div>
  <div class="closure closure--black" style="left:466px; top:668px"></div>
  <div class="closure closure--black" style="left:834px; top:668px"></div>

  <!-- Variant 1 -->
  <svg class="label label--v1" style="left:136px; top:171px" viewBox="-30 0 450 640">
    <rect x="0" y="0" width="389" height="620" rx="12" fill="var(--label-black)"/>
    <g clip-path="url(#label-clip)" role="img" aria-label="Foto: marmoriertes Wagyu-Fleisch">
      <circle cx="194" cy="374" r="245" fill="url(#marble)"/>
    </g>
    <circle cx="194" cy="374" r="210" fill="var(--label-black)"/>
    <text class="brand-name" x="24" y="68" font-size="42" textLength="342" lengthAdjust="spacingAndGlyphs">HOLMBERG FARM</text>
    <text class="tagline" x="24" y="100" font-size="24" textLength="342" lengthAdjust="spacingAndGlyphs">Wagyu Rinder – unsere Passion</text>
    <rect x="64" y="225" width="260" height="290" rx="40" fill="#161616" role="img" aria-label="Strichzeichnung eines Wagyu-Rinderkopfes"/>
    <text class="arc-text arc-text--light fill-red" font-size="34" letter-spacing="14"><textPath href="#arc-top" startOffset="50%" text-anchor="middle">WAGYU</textPath></text>
    <text class="arc-text arc-text--light fill-red" font-size="30" letter-spacing="3"><textPath href="#arc-bottom" startOffset="50%" text-anchor="middle">BOLOGNESE SAUCE</textPath></text>
  </svg>

  <!-- Variant 2 -->
  <svg class="label label--v2" style="left:508px; top:171px" viewBox="-30 0 450 640">
    <g role="img" aria-label="Foto: marmoriertes Wagyu-Fleisch">
      <rect x="0" y="0" width="389" height="620" rx="12" fill="url(#marble-soft)"/>
      <circle cx="194" cy="374" r="243" fill="url(#marble)"/>
    </g>
    <text class="brand-name" x="24" y="68" font-size="42" textLength="342" lengthAdjust="spacingAndGlyphs">HOLMBERG FARM</text>
    <text class="tagline" x="24" y="100" font-size="24" textLength="342" lengthAdjust="spacingAndGlyphs">Wagyu Rinder – unsere Passion</text>
    <rect x="64" y="225" width="260" height="290" rx="40" fill="#3a0f1c" role="img" aria-label="Strichzeichnung eines Wagyu-Rinderkopfes"/>
    <text class="arc-text arc-text--bold fill-red" font-size="40" letter-spacing="16"><textPath href="#arc-top" startOffset="50%" text-anchor="middle">WAGYU</textPath></text>
    <text class="arc-text arc-text--light fill-red" font-size="30" letter-spacing="2"><textPath href="#arc-bottom" startOffset="50%" text-anchor="middle">BOLOGNESE SAUCE</textPath></text>
  </svg>

  <!-- Variant 3 -->
  <svg class="label label--v3" style="left:877px; top:171px" viewBox="-30 0 450 640">
    <rect x="0" y="0" width="389" height="620" rx="12" fill="var(--label-black)"/>
    <g clip-path="url(#label-clip)" role="img" aria-label="Foto: marmoriertes Wagyu-Fleisch">
      <circle cx="194" cy="374" r="240" fill="url(#marble)"/>
    </g>
    <text class="brand-name" x="24" y="68" font-size="42" textLength="342" lengthAdjust="spacingAndGlyphs">HOLMBERG FARM</text>
    <text class="tagline" x="24" y="100" font-size="24" textLength="342" lengthAdjust="spacingAndGlyphs">Wagyu Rinder – unsere Passion</text>
    <rect x="64" y="225" width="260" height="290" rx="40" fill="#3a0f1c" role="img" aria-label="Strichzeichnung eines Wagyu-Rinderkopfes"/>
    <text class="arc-text arc-text--bold fill-white" font-size="40" letter-spacing="16"><textPath href="#arc-top" startOffset="50%" text-anchor="middle">WAGYU</textPath></text>
    <text class="arc-text arc-text--light fill-white" font-size="30" letter-spacing="2"><textPath href="#arc-bottom" startOffset="50%" text-anchor="middle">BOLOGNESE SAUCE</textPath></text>
  </svg>

  <!-- Variant 1, black closure -->
  <svg class="label label--v1" style="left:136px; top:769px" viewBox="-30 0 450 640">
    <rect x="0" y="0" width="389" height="620" rx="12" fill="var(--label-black)"/>
    <g clip-path="url(#label-clip)" role="img" aria-label="Foto: marmoriertes Wagyu-Fleisch">
      <circle cx="194" cy="374" r="245" fill="url(#marble)"/>
    </g>
    <circle cx="194" cy="374" r="210" fill="var(--label-black)"/>
    <text class="brand-name" x="24" y="68" font-size="42" textLength="342" lengthAdjust="spacingAndGlyphs">HOLMBERG FARM</text>
    <text class="tagline" x="24" y="100" font-size="24" textLength="342" lengthAdjust="spacingAndGlyphs">Wagyu Rinder – unsere Passion</text>
    <rect x="64" y="225" width="260" height="290" rx="40" fill="#161616" role="img" aria-label="Strichzeichnung eines Wagyu-Rinderkopfes"/>
    <text class="arc-text arc-text--light fill-red" font-size="34" letter-spacing="14"><textPath href="#arc-top" startOffset="50%" text-anchor="middle">WAGYU</textPath></text>
    <text class="arc-text arc-text--light fill-red" font-size="30" letter-spacing="3"><textPath href="#arc-bottom" startOffset="50%" text-anchor="middle">BOLOGNESE SAUCE</textPath></text>
  </svg>

  <!-- Variant 2, black closure -->
  <svg class="label label--v2" style="left:508px; top:769px" viewBox="-30 0 450 640">
    <g role="img" aria-label="Foto: marmoriertes Wagyu-Fleisch">
      <rect x="0" y="0" width="389" height="620" rx="12" fill="url(#marble-soft)"/>
      <circle cx="194" cy="374" r="243" fill="url(#marble)"/>
    </g>
    <text class="brand-name" x="24" y="68" font-size="42" textLength="342" lengthAdjust="spacingAndGlyphs">HOLMBERG FARM</text>
    <text class="tagline" x="24" y="100" font-size="24" textLength="342" lengthAdjust="spacingAndGlyphs">Wagyu Rinder – unsere Passion</text>
    <rect x="64" y="225" width="260" height="290" rx="40" fill="#3a0f1c" role="img" aria-label="Strichzeichnung eines Wagyu-Rinderkopfes"/>
    <text class="arc-text arc-text--bold fill-red" font-size="40" letter-spacing="16"><textPath href="#arc-top" startOffset="50%" text-anchor="middle">WAGYU</textPath></text>
    <text class="arc-text arc-text--light fill-red" font-size="30" letter-spacing="2"><textPath href="#arc-bottom" startOffset="50%" text-anchor="middle">BOLOGNESE SAUCE</textPath></text>
  </svg>

  <!-- Variant 3, black closure -->
  <svg class="label label--v3" style="left:877px; top:769px" viewBox="-30 0 450 640">
    <rect x="0" y="0" width="389" height="620" rx="12" fill="var(--label-black)"/>
    <g clip-path="url(#label-clip)" role="img" aria-label="Foto: marmoriertes Wagyu-Fleisch">
      <circle cx="194" cy="374" r="240" fill="url(#marble)"/>
    </g>
    <text class="brand-name" x="24" y="68" font-size="42" textLength="342" lengthAdjust="spacingAndGlyphs">HOLMBERG FARM</text>
    <text class="tagline" x="24" y="100" font-size="24" textLength="342" lengthAdjust="spacingAndGlyphs">Wagyu Rinder – unsere Passion</text>
    <rect x="64" y="225" width="260" height="290" rx="40" fill="#3a0f1c" role="img" aria-label="Strichzeichnung eines Wagyu-Rinderkopfes"/>
    <text class="arc-text arc-text--bold fill-white" font-size="40" letter-spacing="16"><textPath href="#arc-top" startOffset="50%" text-anchor="middle">WAGYU</textPath></text>
    <text class="arc-text arc-text--light fill-white" font-size="30" letter-spacing="2"><textPath href="#arc-bottom" startOffset="50%" text-anchor="middle">BOLOGNESE SAUCE</textPath></text>
  </svg>

</main>
</body>
</html>
```